Elevated Kinetic Framework

I am a competitive bodybuilder marketing my articles and videos. I envision a picture of my physique that allows the user to click on different body parts to receive three options: free article, fee based video or fee based personalized routine. I also need a page describing meal planning options that includes videos. Would also like pages for photos and blogging.
I want to maximize site visibility. Many fitness sites use what appears to be a template like this: http://www.marlowtpeck.example/Build-7-8-Kilos-Of-Lean-Tissue.html. I would be interested in incorporating some pages like that.

I have a current site at corbinlusk.example. I have not created video content yet.I can provide my current hosting details if needed. Feel free to contact me to discuss any design questions at corbin@lusk.example or 555 614 8297.

Target Market(s)

health and fitness, weight loss, muscle gain, body building, power lifting, wellness, natural medicine

Industry/Entity Type

Marketing

Requirements
Must have
• I can provide full body photos. Want my business and personal name displayed. Possible flash design that starts small then quickly increases in size on main page?

```html
<!DOCTYPE html>
<html lang="en">
<head>
<meta charset="utf-8">
<title>Corbin Lusk — Truth in Bodybuilding</title>
<link rel="stylesheet" href="https://fonts.googleapis.com/css2?family=Crimson+Text:wght@400;600;700&family=PT+Sans:ital,wght@0,400;0,700;1,400&display=swap">
<style>
  :root {
    --red: #9c0000;
    --red-bright: #c00000;
    --red-dark: #7a0000;
    --ink: #555555;
    --ink-dark: #333333;
    --muted: #6a6a6a;
    --line: #cfcfcf;
    --black: #000000;
    --white: #ffffff;
    --tile: #555555;
  }
  * { box-sizing: border-box; margin: 0; padding: 0; }
  html, body { width: 1108px; height: 1200px; overflow: hidden; background: var(--white); }
  body { position: relative; font-family: "PT Sans", Arial, sans-serif; color: var(--ink); }

  .site-header { position: absolute; left: 0; top: 0; width: 1108px; height: 90px; }
  .brand { position: absolute; left: 111px; top: 16px; }
  .brand-name { font-family: "Crimson Text", Georgia, serif; font-size: 31px; color: var(--red); line-height: 1; font-weight: 400; }
  .brand-tagline { font-size: 13px; color: var(--ink-dark); margin: 7px 0 0 27px; }
  .main-nav { position: absolute; right: 113px; top: 37px; display: flex; gap: 29px; }
  .main-nav a { font-family: "Crimson Text", Georgia, serif; font-weight: 700; font-size: 12.5px; color: var(--ink-dark); text-decoration: none; letter-spacing: .2px; }
  .main-nav a.is-active { color: var(--red); }

  .hero { position: absolute; left: 0; top: 90px; width: 1108px; height: 332px; background: var(--black); }
  .hero-photo { position: absolute; left: 55px; top: 0; width: 305px; height: 332px;
    background: radial-gradient(ellipse at 45% 45%, #c66a2a 0%, #8a4218 40%, #2a140a 75%, #000 100%); }
  .hero-quote { position: absolute; left: 403px; top: 133px; width: 290px; font-style: italic; font-size: 20.5px; line-height: 26px; color: var(--white); }
  .hero-dots { position: absolute; left: 535px; top: 312px; display: flex; gap: 5px; }
  .hero-dots span { width: 9px; height: 9px; border-radius: 50%; background: #b5b5b5; }
  .hero-dots span.is-current { background: #555; }

  .contact-form { position: absolute; left: 711px; top: 12px; width: 258px; height: 309px; background: var(--red); padding: 14px 9px 0 9px; }
  .contact-form h2 { font-family: "Crimson Text", Georgia, serif; font-weight: 700; font-size: 21px; color: var(--white); margin: 0 0 12px 8px; }
  .contact-form label { display: block; font-size: 11.5px; color: var(--white); margin-bottom: 7px; }
  .contact-form .field { width: 240px; height: 35px; background: var(--white); margin-bottom: 12px; }
  .contact-form .submit { position: absolute; right: 10px; bottom: 17px; background: var(--red-bright); color: var(--white); font-weight: 700; font-size: 14px; padding: 8px 11px; }

  .content { position: absolute; left: 111px; top: 434px; width: 582px; }
  .welcome-title { font-size: 18px; color: var(--muted); font-weight: 400; margin-top: 1px; }
  .welcome-title span { color: var(--red); }
  .feature { display: flex; gap: 10px; }
  .photo-fill { flex: none; }
  .body-copy { font-size: 11.5px; line-height: 16.6px; text-align: justify; color: var(--muted); }
  .welcome { margin-top: 17px; }
  .welcome .photo-fill { width: 212px; height: 142px; background: linear-gradient(135deg, #5d3a22, #9a5a34 50%, #4a5a30); }
  .welcome .body-copy { width: 360px; margin-top: -2px; }

  .section-head { border-top: 1px dashed var(--line); border-bottom: 1px dashed var(--line); padding: 7px 0 6px; font-size: 18.5px; color: var(--muted); font-weight: 400; }
  .mass { margin-top: 23px; }
  .section-body { margin-top: 17px; display: flex; gap: 10px; }
  .section-body .photo-fill { width: 286px; height: 165px; position: relative; }
  .section-body .body-copy { width: 286px; font-size: 11.5px; line-height: 14.3px; margin-top: -1px; }
  .mass .photo-fill { background: linear-gradient(180deg, #4a4a3a 0%, #6e4a30 45%, #4e7a30 75%, #3f6a28 100%); }
  .play-icon { position: absolute; left: 102px; top: 52px; }
  .price { font-size: 16px; color: var(--red); margin: 9px 0 9px; }
  .button { display: inline-block; background: var(--red); color: var(--white); font-weight: 700; font-size: 12px; padding: 7px 8px; border: 1px solid var(--red-dark); box-shadow: 0 0 0 1px #e8c0c0; }
  .meal { margin-top: 19px; }
  .meal .photo-fill { background: linear-gradient(90deg, #2a1a10, #8a4a22 30%, #2a1a10 55%, #9a5528 80%, #2a1a10); }
  .meal .body-copy p + p { margin-top: 14px; }
  .meal .button { margin-top: 12px; }

  .sidebar { position: absolute; left: 720px; top: 434px; width: 277px; }
  .widget { border: 1px solid #dcdcdc; }
  .widget-title { background: linear-gradient(180deg, var(--red-bright), var(--red)); color: var(--white); font-size: 18.5px; font-weight: 400; height: 33px; line-height: 33px; padding-left: 9px; }
  .articles { height: 426px; padding: 0 4px 0 4px; }
  .article { border-bottom: 1px dashed var(--line); padding: 9px 0 10px; margin-right: 3px; }
  .article:last-child { border-bottom: none; }
  .article h3 { font-size: 14px; font-weight: 400; color: var(--red); margin-bottom: 9px; }
  .article p { font-size: 11.3px; line-height: 16.6px; color: var(--muted); text-align: justify; }
  .gallery { margin-top: 18px; }
  .gallery-photo { height: 186px; position: relative; background: linear-gradient(90deg, #1a0e08, #8a4a22 25%, #2a160c 50%, #9a5528 75%, #1a0e08); }
  .gallery-nav { position: absolute; left: 115px; top: 140px; }

  .site-footer { position: absolute; left: 111px; top: 1132px; width: 886px; border-top: 1px solid #e4e4e4; }
  .copyright { position: absolute; left: 0; top: 24px; font-size: 11px; color: var(--muted); }
  .social { position: absolute; right: 5px; top: 18px; display: flex; gap: 6px; }
  .social span { width: 26px; height: 26px; background: var(--tile); }
</style>
</head>
<body>
  <header class="site-header">
    <div class="brand">
      <div class="brand-name">Corbin Lusk</div>
      <div class="brand-tagline">"Truth in Bodybuilding"</div>
    </div>
    <nav class="main-nav">
      <a class="is-active" href="#">MY ARTICLES</a>
      <a href="#">VIDEOS</a>
      <a href="#">MEAL PLANNING</a>
      <a href="#">PHOTOGRAPHS</a>
    </nav>
  </header>

  <section class="hero">
    <div class="hero-photo" role="img" aria-label="Bodybuilder posing with arms behind his head on a dark stage"></div>
    <p class="hero-quote">As a lifelong veteran of com-<br>petitive bodybuilding and<br>powerlifting</p>
    <div class="hero-dots"><span></span><span class="is-current"></span><span></span></div>
    <form class="contact-form">
      <h2>Send a Message to Corbin</h2>
      <label>Your email address:</label><div class="field"></div>
      <label>Subject:</label><div class="field"></div>
      <label>Your message:</label><div class="field"></div>
      <div class="submit">SUBMIT</div>
    </form>
  </section>

  <main class="content">
    <h1 class="welcome-title">Welcome to <span>Corbin Lusk !</span></h1>
    <div class="feature welcome">
      <div class="photo-fill" role="img" aria-label="Portrait of a muscular athlete outdoors"></div>
      <p class="body-copy">As a lifelong veteran of competitive bodybuilding and powerlifting, I have learned the hard way that these sports are teeming with misinformation, lies and general dishonesty. The knowledge needed to build a body to its genetic maximum without the use of drugs is very difficult to obtain. I have dedicated my life to the pursuit of this knowledge and now that I have acquired it, I feel it is my obligation to make it available to everyone. This site can allow anyone to achieve their goals without fruitless efforts, injuries and wasted money. I have committed all these errors; now let me show you how to avoid them.</p>
    </div>

    <section class="mass">
      <h2 class="section-head">Mass Building</h2>
      <div class="section-body">
        <div class="photo-fill" role="img" aria-label="Video still of a bodybuilder flexing his back on a lawn">
          <svg class="play-icon" width="106" height="62" viewBox="0 0 106 62"><rect width="106" height="62" rx="6" fill="#ffffff" fill-opacity=".25"/><path d="M42 16 L68 31 L42 46 Z" fill="#ffffff" fill-opacity=".55"/></svg>
        </div>
        <div class="body-copy">
          <p>This routine represents the best method for adding drug free mass for trainees of all backgrounds. This program will result in the addition of not only symmetrical lean mass but also the strength and power prerequisite to such gains. This makes the program ideal for individuals in any sport, not just the iron games. In short, this is the best way to train to develop your body, period.</p>
          <div class="price">Price : $100</div>
          <span class="button">BUY NOW!</span>
        </div>
      </div>
    </section>

    <section class="meal">
      <h2 class="section-head">Meal planning</h2>
      <div class="section-body">
        <div class="photo-fill" role="img" aria-label="Four bodybuilders posing in a line on stage"></div>
        <div class="body-copy">
          <p>This routine represents the best method for adding drug free mass for trainees of all backgrounds.</p>
          <p>This program will result in the addition of not only symmetrical lean mass but also the strength and power prerequisite to such gains. This makes the program ideal for individuals in any sport, not just the iron games. In short, this is the best way to train to develop your body, period.</p>
          <span class="button">View More</span>
        </div>
      </div>
    </section>
  </main>

  <aside class="sidebar">
    <section class="widget">
      <h2 class="widget-title">Recent Article</h2>
      <div class="articles">
        <article class="article"><h3>The Jewel of the Crown</h3><p>Abdominals are the visual centerpiece of the body. They tell everyone immediately what condition you are in. They demand respect unlike any other bodypart because they convey your discipline outside of the</p></article>
        <article class="article"><h3>Effective Fat Loss</h3><p>Many people in the gym have a good idea about how to gain mass, yet nearly everyone seems to be in the dark about getting ripped</p></article>
        <article class="article"><h3>Pump Up Those Forearms!</h3><p>Many people in the gym have a good idea about how to gain mass, yet nearly everyone seems to be in the dark about getting ripped</p></article>
        <article class="article"><h3>General Fitness</h3><p>Many people in the gym have a good idea about how to gain mass, yet nearly everyone seems to be in the dark about getting ripped</p></article>
      </div>
    </section>
    <section class="widget gallery">
      <h2 class="widget-title">Photo Gallery</h2>
      <div class="gallery-photo" role="img" aria-label="Bodybuilders flexing in a posedown on stage">
        <svg class="gallery-nav" width="66" height="38" viewBox="0 0 66 38"><rect x="1" y="1" width="64" height="36" rx="18" fill="#222" stroke="#ccc" stroke-width="2"/><rect x="14" y="8" width="38" height="22" rx="11" fill="#a00000"/><path d="M20 19 L28 14 L28 24 Z M46 19 L38 14 L38 24 Z" fill="#fff"/></svg>
      </div>
    </section>
  </aside>

  <footer class="site-footer">
    <p class="copyright">© 2013 Delia Marsh &nbsp;|&nbsp; All rights reserved.</p>
    <div class="social" aria-label="Social links"><span></span><span></span><span></span><span></span><span></span></div>
  </footer>
</body>
</html>
```